Closed loop end of life cycle for electronics Loop.

Sustainability Closed Loop. I need six sections on the Closed Loop
1-End-of-life Product & Mfg. Scrap
2-OBNE Services
3-Mechanical Processing
4-Precious Metals Refining
5-Metal Products Manufactured
6-Products return to OEMs
Target Market(s)
Vorex, Brindle, KRWP, other major manufacturers of electronics and semiconductor
Industry/Entity Type
Sustainablek
Font styles to use
Serif
Sans Serif
Colors
0054AA
0677BA
7BADD7
CADEEF
E8F1F8
0094D4
00A9DD
6FCCEA
C7EBF8
E9F6FB
00AB8E
00BBA5
67D7C9
C6EFE9
E9F9F6
Requirements
Must have
- Sustainability Closed Loop. I need six sections on the Closed Loop ring below.

```html
<!DOCTYPE html>
<html lang="en">
<head>
<meta charset="utf-8">
<title>Sustainability Closed Loop</title>
<link rel="stylesheet" href="https://fonts.googleapis.com/css2?family=EB+Garamond:wght@500&family=Crimson+Pro:wght@700&display=swap">
<style>
  :root {
    --page: #ffffff;
    --title: #000000;
    --label: #ffffff;
    --ring-shadow: #b3b3b3;

    --eol-deep: #0c3f80;
    --eol-mid: #1a56a0;
    --eol-light: #6aaee8;

    --svc-deep: #14619f;
    --svc-mid: #1468ae;
    --svc-light: #b6f2fc;

    --mech-deep: #1286cc;
    --mech-mid: #1a8fd4;
    --mech-light: #bdf2fc;

    --refine-deep: #0e7f69;
    --refine-mid: #0f8a72;
    --refine-light: #58d9c1;

    --mfg-deep: #0f9f87;
    --mfg-mid: #1aaa92;
    --mfg-light: #c6fff9;

    --return-deep: #5acdbd;
    --return-mid: #70d9c9;
    --return-light: #c2f6ea;
  }
  html, body {
    margin: 0;
    padding: 0;
    width: 1200px;
    height: 1184px;
    overflow: hidden;
    background: var(--page);
  }
  .loop-diagram {
    display: block;
    width: 1200px;
    height: 1184px;
  }
  .loop-title {
    font-family: "Crimson Pro", "Times New Roman", serif;
    font-weight: 700;
    font-size: 108px;
    fill: var(--title);
    text-anchor: middle;
    letter-spacing: 1px;
  }
  .stage-label {
    font-family: "EB Garamond", Georgia, serif;
    font-weight: 500;
    font-size: 56px;
    fill: var(--label);
    letter-spacing: 1px;
  }
  .stage-label--single { font-size: 62px; }
  .ring-shadow {
    fill: none;
    stroke: var(--ring-shadow);
    stroke-width: 10;
  }
</style>
</head>
<body>
<svg class="loop-diagram" viewBox="0 12 1932 1907" xmlns="http://www.w3.org/2000/svg" role="img" aria-label="Sustainability closed loop with six stages">
  <defs>
    <linearGradient id="grad-eol" gradientUnits="userSpaceOnUse" x1="310" y1="1012" x2="772" y2="324">
      <stop offset="0" stop-color="var(--eol-deep)"/>
      <stop offset="0.55" stop-color="var(--eol-mid)"/>
      <stop offset="1" stop-color="var(--eol-light)"/>
    </linearGradient>
    <linearGradient id="grad-svc" gradientUnits="userSpaceOnUse" x1="588" y1="416" x2="1415" y2="472">
      <stop offset="0" stop-color="var(--svc-deep)"/>
      <stop offset="0.55" stop-color="var(--svc-mid)"/>
      <stop offset="1" stop-color="var(--svc-light)"/>
    </linearGradient>
    <linearGradient id="grad-mech" gradientUnits="userSpaceOnUse" x1="1243" y1="359" x2="1608" y2="1104">
      <stop offset="0" stop-color="var(--mech-deep)"/>
      <stop offset="0.55" stop-color="var(--mech-mid)"/>
      <stop offset="1" stop-color="var(--mech-light)"/>
    </linearGradient>
    <linearGradient id="grad-refine" gradientUnits="userSpaceOnUse" x1="1620" y1="898" x2="1158" y2="1586">
      <stop offset="0" stop-color="var(--refine-deep)"/>
      <stop offset="0.55" stop-color="var(--refine-mid)"/>
      <stop offset="1" stop-color="var(--refine-light)"/>
    </linearGradient>
    <linearGradient id="grad-mfg" gradientUnits="userSpaceOnUse" x1="1342" y1="1494" x2="515" y2="1438">
      <stop offset="0" stop-color="var(--mfg-deep)"/>
      <stop offset="0.55" stop-color="var(--mfg-mid)"/>
      <stop offset="1" stop-color="var(--mfg-light)"/>
    </linearGradient>
    <linearGradient id="grad-return" gradientUnits="userSpaceOnUse" x1="687" y1="1551" x2="322" y2="807">
      <stop offset="0" stop-color="var(--return-deep)"/>
      <stop offset="0.55" stop-color="var(--return-mid)"/>
      <stop offset="1" stop-color="var(--return-light)"/>
    </linearGradient>
    <filter id="head-shadow" x="-20%" y="-20%" width="140%" height="140%">
      <feDropShadow dx="-10" dy="8" stdDeviation="3" flood-color="#000" flood-opacity="0.3"/>
    </filter>

    <!-- label baselines -->
    <path id="path-eol-outer" d="M282.6 1014.7 A685 685 0 0 1 905.3 272.6"/>
    <path id="path-eol-inner" d="M362.3 1007.8 A605 605 0 0 1 912.2 352.3"/>
    <path id="path-svc" d="M600.8 434.8 A635 635 0 0 1 1485.2 590.8"/>
    <path id="path-mech-outer" d="M1176.7 303.5 A685 685 0 0 1 1616.5 1166.7"/>
    <path id="path-mech-inner" d="M1152 379.6 A605 605 0 0 1 1540.4 1141.9"/>
    <path id="path-refine-outer" d="M1632.5 800.9 A685 685 0 0 1 1119.1 1622.5"/>
    <path id="path-refine-inner" d="M1554.5 818.9 A605 605 0 0 1 1101.1 1544.5"/>
    <path id="path-mfg-inner" d="M523.1 1396.9 A625 625 0 0 0 1406.9 1396.9"/>
    <path id="path-mfg-outer" d="M462.9 1457 A710 710 0 0 0 1467 1457"/>
    <path id="path-return-outer" d="M742 1602.7 A685 685 0 0 1 317.3 732"/>
    <path id="path-return-inner" d="M768 1527 A605 605 0 0 1 392.9 758"/>
  </defs>

  <circle class="ring-shadow" cx="965" cy="955" r="557"/>

  <g class="ring-bodies">
    <path class="segment segment--eol" fill="url(#grad-eol)" d="M412.1 1003.4 L207.9 1021.3 A760 760 0 0 1 529.1 332.4 L646.7 500.3 A555 555 0 0 0 412.1 1003.4 Z"/>
    <path class="segment segment--services" fill="url(#grad-svc)" d="M646.7 500.3 L529.1 332.4 A760 760 0 0 1 1286.2 266.2 L1199.5 452 A555 555 0 0 0 646.7 500.3 Z"/>
    <path class="segment segment--mechanical" fill="url(#grad-mech)" d="M1199.5 452 L1286.2 266.2 A760 760 0 0 1 1722.1 888.7 L1517.9 906.6 A555 555 0 0 0 1199.5 452 Z"/>
    <path class="segment segment--refining" fill="url(#grad-refine)" d="M1517.9 906.6 L1722.1 888.7 A760 760 0 0 1 1400.9 1577.6 L1283.3 1409.7 A555 555 0 0 0 1517.9 906.6 Z"/>
    <path class="segment segment--manufacturing" fill="url(#grad-mfg)" d="M1283.3 1409.7 L1400.9 1577.6 A760 760 0 0 1 643.8 1643.8 L730.5 1458 A555 555 0 0 0 1283.3 1409.7 Z"/>
    <path class="segment segment--return" fill="url(#grad-return)" d="M730.5 1458 L643.8 1643.8 A760 760 0 0 1 207.9 1021.3 L412.1 1003.4 A555 555 0 0 0 730.5 1458 Z"/>
  </g>

  <g class="ring-heads" filter="url(#head-shadow)">
    <path class="arrowhead" fill="url(#grad-eol)" d="M692.5 565.9 L490.6 277.5 L772 323.8 Z"/>
    <path class="arrowhead" fill="url(#grad-svc)" d="M1165.7 524.5 L1314.5 205.5 L1415.1 472.3 Z"/>
    <path class="arrowhead" fill="url(#grad-mech)" d="M1438.2 913.6 L1788.9 882.9 L1608.1 1103.5 Z"/>
    <path class="arrowhead" fill="url(#grad-refine)" d="M1237.5 1344.1 L1439.4 1632.5 L1158 1586.2 Z"/>
    <path class="arrowhead" fill="url(#grad-mfg)" d="M764.3 1385.5 L615.5 1704.5 L514.9 1437.7 Z"/>
    <path class="arrowhead" fill="url(#grad-return)" d="M491.8 996.4 L141.1 1027.1 L321.9 806.5 Z"/>
  </g>

  <g class="stage-labels">
    <text class="stage-label"><textPath href="#path-eol-outer" startOffset="50%" text-anchor="middle">End-of-life Product</textPath></text>
    <text class="stage-label"><textPath href="#path-eol-inner" startOffset="50%" text-anchor="middle">&amp; Mfg. Scrap</textPath></text>

    <text class="stage-label stage-label--single"><textPath href="#path-svc" startOffset="50%" text-anchor="middle">OBNE Services</textPath></text>

    <text class="stage-label"><textPath href="#path-mech-outer" startOffset="50%" text-anchor="middle">Mechanical</textPath></text>
    <text class="stage-label"><textPath href="#path-mech-inner" startOffset="50%" text-anchor="middle">Processing</textPath></text>

    <text class="stage-label"><textPath href="#path-refine-outer" startOffset="50%" text-anchor="middle">Precious Metals</textPath></text>
    <text class="stage-label"><textPath href="#path-refine-inner" startOffset="50%" text-anchor="middle">Refining</textPath></text>

    <text class="stage-label"><textPath href="#path-mfg-inner" startOffset="50%" text-anchor="middle">Metal Products</textPath></text>
    <text class="stage-label"><textPath href="#path-mfg-outer" startOffset="50%" text-anchor="middle">Manufactured</textPath></text>

    <text class="stage-label"><textPath href="#path-return-outer" startOffset="50%" text-anchor="middle">Products Return</textPath></text>
    <text class="stage-label"><textPath href="#path-return-inner" startOffset="50%" text-anchor="middle">to OEMs</textPath></text>
  </g>

  <g class="loop-heading">
    <text class="loop-title" x="965" y="855">SUSTAINABILITY</text>
    <text class="loop-title" x="965" y="1020">CLOSED</text>
    <text class="loop-title" x="965" y="1185">LOOP</text>
  </g>
</svg>
</body>
</html>
```